Sales Page Header Design Project

Hi,
I need a background image created for this sales page: http://corvellatrainingcamp.com
Width: 977 px
Height: 150 px
Here are a few sample designs to work with: http://mintwaterstudiohall.com/
http://paintingthefenceweb.com/wp-content/uploads/2011/02/experts1.png
Must be sharp, professional looking and uncluttered.
Colours: Must include blue (I like the blue on the on the current sales page, but will leave shade and colour combinations to your creativity)
Text = Tobi Marvenko Presents
Corvella Training Camp
Your Blueprint for Building a Profitable, Sustainable Business in Today's Economy!
Any questions, give me a shout
Entrepreneurs and Business Owners, aged 21 to 45
Business

```html
<!DOCTYPE html>
<html lang="en">
<head>
<meta charset="utf-8">
<title>Corvella Training Camp</title>
<link rel="stylesheet" href="https://fonts.googleapis.com/css2?family=Roboto+Condensed:ital,wght@0,700;1,400&family=Gelasio:wght@700&family=Arimo:ital,wght@0,400;1,700&display=swap">
<style>
  :root {
    --band-dark: #0a5fb0;
    --band-light: #1aa3e0;
    --sky-top: #1f86dc;
    --sky-mid: #6cc0f0;
    --cloud: rgba(245,249,253,0.9);
    --city: rgba(120,140,165,0.85);
    --grass: #7cc63a;
    --grass-dark: #5aa82a;
    --headline-red: #cc0000;
    --form-blue: #1f5d8c;
    --body-grey: #666666;
    --field-border: #c8c8c8;
    --button-yellow: #ffe23a;
    --button-gold: #f5c400;
    --button-text: #12305a;
    --swoosh-blue: #1b4fa8;
    --footer-red: #7a1010;
  }
  * { box-sizing: border-box; margin: 0; padding: 0; }
  html, body { width: 1200px; height: 643px; overflow: hidden; background: #ffffff; }
  .page { position: relative; width: 1200px; height: 643px; font-family: "Arimo", Arial, sans-serif; }

  .top-band {
    position: absolute; left: 0; top: 0; width: 1200px; height: 144px;
    background: linear-gradient(180deg, var(--band-dark) 0%, var(--band-light) 100%);
  }
  .banner {
    position: absolute; left: 127px; top: 0; width: 937px; height: 144px; overflow: hidden;
    background: linear-gradient(180deg, var(--sky-top) 0%, var(--sky-mid) 72%, var(--grass) 84%, var(--grass-dark) 100%);
  }
  .banner-scene {
    position: absolute; left: 0; top: 0; width: 937px; height: 144px;
    background:
      radial-gradient(ellipse 260px 70px at 660px 50px, var(--cloud) 0%, rgba(245,249,253,0) 100%),
      linear-gradient(180deg, rgba(0,0,0,0) 0%, rgba(0,0,0,0) 40%, var(--city) 62%, var(--city) 72%, rgba(110,180,60,0) 84%);
    -webkit-mask-image: linear-gradient(90deg, transparent 0px, transparent 420px, #000 560px);
    mask-image: linear-gradient(90deg, transparent 0px, transparent 420px, #000 560px);
  }
  .banner-presenter {
    position: absolute; left: 11px; top: 11px; color: #fff;
    font-family: "Roboto Condensed", "Arial Narrow", sans-serif; font-weight: 700; font-size: 20px; line-height: 24px;
  }
  .banner-title {
    position: absolute; left: 11px; top: 34px; color: #fff; text-transform: uppercase;
    font-family: "Roboto Condensed", "Arial Narrow", sans-serif; font-weight: 700; font-size: 33px; line-height: 40px; letter-spacing: 0.3px;
  }
  .banner-tagline {
    position: absolute; left: 12px; top: 76px; width: 420px; color: #fff;
    font-family: "Roboto Condensed", "Arial Narrow", sans-serif; font-style: italic; font-weight: 400; font-size: 14px; line-height: 17px;
  }

  .headline {
    position: absolute; left: 148px; top: 168px; width: 600px; text-align: center;
    font-family: "Gelasio", Georgia, serif; font-weight: 700; font-size: 43px; line-height: 44px;
    color: var(--headline-red);
  }

  .video {
    position: absolute; left: 150px; top: 269px; width: 605px; height: 343px;
    background: #000; border: 1px solid #cfcfcf;
  }
  .video-board {
    position: absolute; left: 75px; top: 0; width: 454px; height: 341px;
    background: linear-gradient(180deg, #c9c9c9 0px, #f4f4f4 8px, #e6e6e6 14px, #f7f7f7 20px, #ffffff 60%, #f1f1f1 312px, #e6e6e6 320px, #f6f6f6 326px, #c9c9c9 341px);
  }
  .play-button {
    position: absolute; left: 277px; top: 146px; width: 48px; height: 48px;
    background: rgba(40,40,40,0.85);
  }
  .play-button svg { display: block; }

  .pointer-arrow { position: absolute; left: 850px; top: 144px; }

  .signup { position: absolute; left: 797px; top: 316px; width: 252px; }
  .signup-title { text-align: center; color: var(--form-blue); font-size: 19px; line-height: 26px; }
  .signup-text { margin: 8px 0 0 5px; color: var(--body-grey); font-size: 13.5px; line-height: 19px; }
  .field {
    position: absolute; left: 0; width: 252px; height: 41px; border: 2px solid var(--field-border);
    padding: 0 11px; font-size: 17px; line-height: 37px; color: #222;
  }
  .field-name { top: 102px; }
  .field-email { top: 152px; }
  .swoosh { position: absolute; left: 2px; top: 208px; }
  .register-button {
    position: absolute; left: 0; top: 227px; width: 249px; height: 56px; border-radius: 5px;
    border: 1px solid #d9a800;
    background: linear-gradient(180deg, #fff7a8 0%, var(--button-yellow) 45%, var(--button-gold) 100%);
    text-align: center; font-style: italic; font-weight: 700; font-size: 24px; line-height: 54px;
    color: var(--button-text); letter-spacing: -0.5px;
  }

  .footer-line { position: absolute; left: 0; top: 640px; width: 1200px; height: 3px; background: var(--footer-red); }
  .footer-tab {
    position: absolute; left: 555px; top: 634px; width: 47px; height: 9px; border-radius: 6px 6px 0 0;
    background: linear-gradient(180deg, #a9c4e6, #6e93c8);
  }
</style>
</head>
<body>
<div class="page">
  <header class="top-band">
    <div class="banner">
      <div class="banner-scene" role="img" aria-label="City skyline of tall glass towers under a cloudy blue sky, with green trees and lawn in front"></div>
      <div class="banner-presenter">Tobi Marvenko Presents</div>
      <div class="banner-title">Corvella Training Camp</div>
      <div class="banner-tagline">Your Blueprint for Building a Profitable, Sustainable Business in Today's Economy!</div>
    </div>
  </header>

  <h1 class="headline">Do You Make These Costly Mistakes In Business?</h1>

  <div class="video">
    <div class="video-board" role="img" aria-label="Whiteboard animation still with handwritten intro line and a small figure stepping across stones between shark fins"></div>
    <div class="play-button">
      <svg width="48" height="48" viewBox="0 0 48 48"><polygon points="18,14 34,24 18,34" fill="#ffffff"/></svg>
    </div>
  </div>

  <svg class="pointer-arrow" width="134" height="144" viewBox="0 0 134 144">
    <defs>
      <linearGradient id="arrowFill" x1="0" x2="1" y1="0" y2="0">
        <stop offset="0" stop-color="#e01010"/>
        <stop offset="0.5" stop-color="#ff2a2a"/>
        <stop offset="0.5" stop-color="#c80000"/>
        <stop offset="1" stop-color="#a80000"/>
      </linearGradient>
    </defs>
    <polygon points="35,0 99,0 99,56 134,56 67,144 0,56 35,56" fill="url(#arrowFill)"/>
  </svg>

  <form class="signup">
    <div class="signup-title">Register Here Now...</div>
    <p class="signup-text">Enter Your Name and Email Below to Register for this Business and Life Changing Event!</p>
    <div class="field field-name">Your First Name...</div>
    <div class="field field-email">Your Email...</div>
    <svg class="swoosh" width="232" height="90" viewBox="0 0 232 90">
      <path d="M150,4 C70,2 10,18 12,46 C14,74 80,86 130,84 C180,82 222,70 224,46" fill="none" stroke="var(--swoosh-blue)" stroke-width="2.5"/>
    </svg>
    <div class="register-button">Register Now!</div>
  </form>

  <div class="footer-line"></div>
  <div class="footer-tab"></div>
</div>
</body>
</html>
```